App Design for FlavorTrek

We need an app design for a new app called FlavorTrek, which is an app designed to inspire exploration through personalized recipe generation, local restaurant discoveries, and a vibrant community platform. It caters to food enthusiasts looking to explore global cuisines or find the best local dining spots, offering a premium experience with selected features available for free.

-------UPDATED-----
This app will be AI Driven and may not be heavily dependent on media (images,videos) at first, especially for the Recipe generator feature. Our goal is to still have attractive UI. The core functionalities we are looking are the following
1. Recipe Generator: Either user choose a specific cuisine(italian,spanish), or user inputs ingredients and get recipe, or get recipe for different occasions (xmas, thanksgiving ) and get a randomly get recipe to cook, plain simple. We expect the recipes to be displayed in clear and not too generic manner starting with ingredients and expected duration at top and then step by step guide. We also intend to enable premium users to have playful action button or icon to get unlimited recipes generated until they find what they like and also have save for later feature. These premium features should be disabled for free users and prompted to subscribe if they click them with nice popup
2. Restaurant Recommendation - will have selected pictures and will be based on inputs such as zip code and other filters such as cousine types. Premium users can filter by price range, get unlimited recommendation, see actual price range in the recommendation and can save for later where they can find it later. Free users cannot filter by price (disabled) and should see it hidden in the recommendation
3. Meal Planning - will include just simple and random meal plan with just one button or limited interaction for free, users need to subscribe to get features such as customized plan such as considering allergies or diet preferences. Premium users can also get a shopping checklist of ingredients for weekly meal preps and their step by step guide for each meal recipe.
2. Community Sharing: users can view posts and engage with community content
Updates

Hello Designers,

The initial price was not fair for the work. So I have increased it. There will also be $50-100 bonus for those who come up with great designs or for those who incorporate interesting stuff. Thank you! Much appreciated 🙏

Colors
0054AA
0677BA
7BADD7
CADEEF
E8F1F8
0094D4
00A9DD
6FCCEA
C7EBF8
E9F6FB
00AB8E
00BBA5
67D7C9
C6EFE9
E9F9F6
FFC000
F8CF3A
FAE287
FDF2CF
FEFAEE
F0912C
F2A743
F7CA91
FBE8D2
FDF5EE
EE7325
F08F49
F5BC92
FAE3D3
FDF4ED
A7469A
B969AE
D3A5CF
EDDBEB
F8F0F9
6B429C
8869AF
B7A5CE
E3DAEB
F3F0F8

```html
<!DOCTYPE html>
<html lang="en">
<head>
<meta charset="utf-8">
<title>FlavorTrek – App Screens</title>
<link href="https://fonts.googleapis.com/css2?family=Poppins:wght@400;500;600;700&display=swap" rel="stylesheet">
<style>
:root{
  --bg:#251a12;
  --bg-2:#33241a;
  --orange:#ee7325;
  --orange-2:#f0912c;
  --orange-3:#f2a743;
  --peach:#fbe8d2;
  --cream:#fdf5ee;
  --ink:#1d1d1f;
  --muted:#8a8a8a;
  --line:#e6e6e6;
  --red:#e53935;
  --white:#ffffff;
  --label:#cfc6bf;
}
*{box-sizing:border-box;margin:0;padding:0}
html,body{width:1200px;height:2733px;overflow:hidden}
body{
  font-family:"Poppins",sans-serif;
  background:radial-gradient(ellipse at 50% 30%,var(--bg-2),var(--bg) 70%);
  position:relative;color:var(--ink);
}
.section-label{
  position:absolute;writing-mode:vertical-rl;transform:rotate(180deg);
  font-size:8.5px;letter-spacing:5px;color:var(--label);font-weight:500;white-space:nowrap;
}
.screen{
  position:absolute;width:218px;background:var(--white);border-radius:22px;overflow:hidden;
  box-shadow:0 0 0 4px #111,0 10px 30px rgba(0,0,0,.4);
}
.status{
  position:absolute;top:0;left:0;right:0;height:30px;display:flex;justify-content:space-between;
  align-items:center;padding:0 20px 0 26px;font-size:9px;font-weight:600;z-index:3;
}
.status.light{color:var(--white)}
.status svg{width:36px;height:9px}
.home-bar{position:absolute;bottom:8px;left:50%;width:70px;height:3px;margin-left:-35px;border-radius:2px;background:var(--ink)}
.hdr{
  position:relative;height:92px;
  background:linear-gradient(180deg,var(--orange) 0%,var(--orange-2) 100%);
  border-radius:0 0 50% 50% / 0 0 34px 34px;
}
.hdr-title{position:absolute;top:40px;left:0;right:0;text-align:center;color:var(--white);font-size:10px;font-weight:500}
.round-btn{
  position:absolute;top:38px;width:20px;height:20px;border-radius:50%;border:1.5px solid var(--white);
  display:flex;align-items:center;justify-content:center;
}
.round-btn svg{width:10px;height:10px}
.round-btn.left{left:14px}.round-btn.right{right:14px}
.hero{
  position:absolute;left:50%;border-radius:50%;
  background:radial-gradient(circle,#b8521e 0%,#8a3a14 45%,#f4e7d8 62%,#ffffff 70%);
  box-shadow:0 4px 12px rgba(0,0,0,.18);border:4px solid var(--white);
}
.hero.small{width:68px;height:68px;margin-left:-34px;top:72px;
  background:radial-gradient(circle,#7e8a2e 0%,#b5652a 40%,#f6efe6 70%)}
.hero.big{width:118px;height:118px;margin-left:-59px;top:40px}
.pad{padding:0 14px}
.h-sec{font-size:8.5px;font-weight:600;margin-bottom:8px}
.tabs{display:flex;gap:7px;margin-bottom:24px}
.tab{flex:1;height:44px;border:1px solid var(--line);border-radius:5px;display:flex;flex-direction:column;align-items:center;justify-content:center;gap:4px;font-size:5px;color:var(--muted)}
.tab svg{width:12px;height:12px}
.tab.on{border-color:var(--orange);color:var(--orange)}
.list{border-left:1.5px solid var(--line);padding-left:9px;margin-bottom:30px}
.list-row{display:flex;justify-content:space-between;align-items:center;height:21px;font-size:7px}
.x{color:var(--red);font-size:10px;line-height:1}
.add-row{display:flex;align-items:center;gap:6px;height:21px;font-size:7px;color:#c9c9c9}
.plus{width:10px;height:10px;border-radius:50%;background:var(--orange);color:var(--white);font-size:9px;line-height:10px;text-align:center}
.pills{display:flex;gap:7px;margin-bottom:26px}
.pill{flex:1;height:22px;border:1px solid var(--line);border-radius:5px;font-size:7px;display:flex;align-items:center;justify-content:center}
.pill.on{border-color:var(--orange);color:var(--orange)}
.pills.off .pill{color:#cfcfcf;border-color:#efefef}
.cta{
  height:24px;border-radius:12px;background:linear-gradient(90deg,var(--orange-2),var(--orange));
  color:var(--white);font-size:7px;font-weight:600;display:flex;align-items:center;justify-content:center;gap:6px;
}
.cta .tick{width:11px;height:11px;border-radius:50%;border:1px solid var(--white);font-size:6px;line-height:9px;text-align:center}
.subscribe{position:relative;margin-top:26px;border-top:1px solid #f1f1f1;text-align:center;padding-top:22px}
.subscribe .bell{position:absolute;top:-14px;left:50%;margin-left:-14px;width:28px;height:28px;border-radius:50%;background:var(--white);box-shadow:0 2px 8px rgba(0,0,0,.12);display:flex;align-items:center;justify-content:center}
.subscribe .bell i{width:10px;height:10px;border-radius:50%;background:var(--orange-2);display:block}
.subscribe p{font-size:6px;color:var(--orange);font-weight:600}
.cuisines{display:grid;grid-template-columns:1fr 1fr;gap:7px 7px;margin-bottom:26px}
.cuisine{height:21px;border:1px solid var(--line);border-radius:4px;font-size:7px;display:flex;align-items:center;justify-content:center}
.cuisine.on{border-color:var(--orange);color:var(--orange)}
/* main */
.main-greet{position:absolute;top:84px;left:14px}
.main-greet small{font-size:7px;display:block}
.main-greet h1{font-size:15px;font-weight:700;margin-top:2px}
.avatar{position:absolute;top:40px;left:14px;width:24px;height:24px;border-radius:50%;background:linear-gradient(135deg,#6a8fb8,#c9a887)}
.menu-btn{position:absolute;top:42px;right:14px;width:20px;height:20px;border-radius:50%;background:var(--cream);display:flex;align-items:center;justify-content:center}
.menu-btn svg{width:9px;height:9px}
.blob{position:absolute;top:110px;left:0;width:120px;height:320px}
.option{position:absolute;display:flex;align-items:center;gap:10px;font-size:8px;font-weight:500}
.option .art{width:64px;height:64px;border-radius:50%;border:4px solid var(--white);box-shadow:0 3px 10px rgba(0,0,0,.18)}
.option .go{width:16px;height:16px;border-radius:50%;background:var(--orange);color:var(--white);font-size:9px;display:flex;align-items:center;justify-content:center}
/* details */
.d-kicker{font-size:7px;color:var(--muted);margin-top:12px}
.d-title{font-size:10.5px;font-weight:600;margin:2px 0 6px}
.info{display:flex;border:1px solid var(--line);border-radius:4px;height:34px;margin-bottom:22px}
.info div{flex:1;display:flex;align-items:center;justify-content:center;gap:6px}
.info div+div{border-left:1px solid var(--line)}
.info .ic{width:12px;height:12px;border-radius:50%;background:#d8d8d8}
.info small{display:block;font-size:4.5px;color:var(--muted)}
.info b{font-size:7px;font-weight:600}
.acc{display:flex;justify-content:space-between;align-items:center;font-size:8px;font-weight:600;height:20px;margin-bottom:18px}
.acc svg{width:9px;height:9px}
.acc.open{margin-bottom:4px}
.sub{font-size:6.5px;color:var(--muted);margin:6px 0 6px}
.ing{border-left:1.5px solid var(--line);padding-left:9px;margin-bottom:10px}
.ing p{font-size:6px;height:17.5px;line-height:17.5px}
.step{display:flex;border:1px solid #f0f0f0;border-radius:4px;margin-bottom:6px;box-shadow:0 1px 4px rgba(0,0,0,.04)}
.step b{width:26px;display:flex;align-items:center;justify-content:center;font-size:7px;color:var(--orange);border-right:1px solid #f0f0f0}
.step p{flex:1;font-size:5.8px;line-height:1.55;padding:8px 10px}
.nut{border:1px solid #555;padding:10px 9px 6px;margin:8px 0 24px}
.nut h2{font-size:17px;font-weight:600;line-height:1.15;letter-spacing:.5px}
.nut .r{font-size:6.5px;padding:5px 0;border-bottom:1px solid #e5e5e5}
.nut .r.in{padding-left:6px}
.nut .thick{height:8px;background:#222;margin:4px 0}
.nut .thin{height:4px;background:#222;margin:3px 0}
.nut em{font-size:6.5px;color:var(--muted);display:block;padding:4px 0}
</style>
</head>
<body>

<!-- Labels -->
<div class="section-label" style="left:18px;top:730px">MAIN SCREEN</div>
<div class="section-label" style="left:313px;top:730px">GET A RECIPE SCREEN - SUBSCRIBED</div>
<div class="section-label" style="left:608px;top:730px">GET A RECIPE SCREEN - NOT SUBSCRIBED</div>
<div class="section-label" style="left:903px;top:730px">CHOOSE CUISINETYPE SCREEN</div>
<div class="section-label" style="left:165px;top:1610px">RECIPE DETAILS SCREEN</div>
<div class="section-label" style="left:460px;top:1610px">RECIPE DETAILS SCREEN</div>
<div class="section-label" style="left:755px;top:1610px">RECIPE DETAILS SCREEN</div>

<!-- Main screen -->
<section class="screen" style="left:48px;top:730px;height:470px">
  <div class="status"><span>9:41</span><svg viewBox="0 0 36 9"><rect x="0" y="5" width="2" height="4"/><rect x="3" y="3" width="2" height="6"/><rect x="6" y="1" width="2" height="8"/><rect x="24" y="1" width="11" height="7" rx="2"/></svg></div>
  <div class="avatar"></div>
  <div class="menu-btn"><svg viewBox="0 0 9 9"><path d="M1 2h7M1 4.5h7M1 7h7" stroke="#ee7325" stroke-width="1"/></svg></div>
  <div class="main-greet"><small>Hi Marlo,</small><h1>What’d you like today?</h1></div>
  <svg class="blob" viewBox="0 0 120 320" preserveAspectRatio="none"><path d="M0 40 Q40 30 60 60 Q20 120 70 170 Q100 200 60 240 Q10 270 30 320 L0 320Z" fill="#f08f49"/></svg>
  <div class="option" style="top:130px;left:16px"><div class="art" role="img" aria-label="Illustration of a recipe dish with herbs" style="background:radial-gradient(circle,#8c5a2a,#6f8a2f 50%,#f6efe6 72%)"></div>Get a recipe <span class="go">→</span></div>
  <div class="option" style="top:235px;left:48px"><div class="art" role="img" aria-label="Illustration of restaurant dining icon" style="background:radial-gradient(circle,#f2a743,#ee7325 55%,#fdf4ed 72%)"></div>Eat out <span class="go">→</span></div>
  <div class="option" style="top:340px;left:16px"><div class="art" role="img" aria-label="Illustration of a meal planner calendar" style="background:radial-gradient(circle,#7badd7,#cadeef 55%,#ffffff 72%)"></div>Plan a meal <span class="go">→</span></div>
  <div class="home-bar"></div>
</section>

<!-- Get a recipe - subscribed -->
<section class="screen" style="left:343px;top:730px;height:545px">
  <div class="status light"><span>9:41</span><svg viewBox="0 0 36 9" fill="#fff"><rect x="0" y="5" width="2" height="4"/><rect x="3" y="3" width="2" height="6"/><rect x="6" y="1" width="2" height="8"/><rect x="24" y="1" width="11" height="7" rx="2"/></svg></div>
  <div class="hdr"><div class="hdr-title">Get a recipe</div><div class="round-btn left"><svg viewBox="0 0 10 10"><path d="M8 5H2M5 2L2 5l3 3" stroke="#fff" fill="none"/></svg></div></div>
  <div class="hero small" role="img" aria-label="Recipe illustration with herbs and vegetables"></div>
  <div class="pad" style="margin-top:68px">
    <div class="h-sec">Customize your recipe</div>
    <div class="tabs"><div class="tab on"><svg viewBox="0 0 12 12"><path d="M2 10l7-7 1 1-7 7z" fill="#ee7325"/></svg>Add Ingredients</div><div class="tab"><svg viewBox="0 0 12 12"><path d="M1 9h10M2 9a4 4 0 018 0" fill="#ccc"/></svg>Cuisine</div><div class="tab"><svg viewBox="0 0 12 12"><rect x="2" y="5" width="8" height="5" fill="#ccc"/></svg>Occasion</div></div>
    <div class="h-sec">Add your ingredients</div>
    <div class="list">
      <div class="list-row">Beef<span class="x">×</span></div>
      <div class="list-row">Onions<span class="x">×</span></div>
      <div class="list-row">Tomatoes<span class="x">×</span></div>
      <div class="list-row">Capsicum<span class="x">×</span></div>
      <div class="add-row"><span class="plus">+</span>add ingredient</div>
    </div>
    <div class="h-sec">Maximum Cooking Time</div>
    <div class="pills"><div class="pill">30 mins</div><div class="pill on">1 hr</div><div class="pill">2 hrs</div></div>
    <div class="cta"><span class="tick">✓</span>Get your recipe</div>
  </div>
  <div class="home-bar"></div>
</section>

<!-- Get a recipe - not subscribed -->
<section class="screen" style="left:638px;top:730px;height:615px">
  <div class="status light"><span>9:41</span><svg viewBox="0 0 36 9" fill="#fff"><rect x="0" y="5" width="2" height="4"/><rect x="3" y="3" width="2" height="6"/><rect x="6" y="1" width="2" height="8"/><rect x="24" y="1" width="11" height="7" rx="2"/></svg></div>
  <div class="hdr"><div class="hdr-title">Get a recipe</div><div class="round-btn left"><svg viewBox="0 0 10 10"><path d="M8 5H2M5 2L2 5l3 3" stroke="#fff" fill="none"/></svg></div></div>
  <div class="hero small" role="img" aria-label="Recipe illustration with herbs and vegetables"></div>
  <div class="pad" style="margin-top:68px">
    <div class="h-sec">Customize your recipe</div>
    <div class="tabs"><div class="tab on"><svg viewBox="0 0 12 12"><path d="M2 10l7-7 1 1-7 7z" fill="#ee7325"/></svg>Add Ingredients</div><div class="tab"><svg viewBox="0 0 12 12"><path d="M1 9h10M2 9a4 4 0 018 0" fill="#ccc"/></svg>Cuisine</div><div class="tab"><svg viewBox="0 0 12 12"><rect x="2" y="5" width="8" height="5" fill="#ccc"/></svg>Occasion</div></div>
    <div class="h-sec">Add your ingredients</div>
    <div class="list">
      <div class="list-row">Beef<span class="x">×</span></div>
      <div class="list-row">Onions<span class="x">×</span></div>
      <div class="list-row">Tomatoes<span class="x">×</span></div>
      <div class="list-row">Capsicum<span class="x">×</span></div>
      <div class="add-row"><span class="plus">+</span>add ingredient</div>
    </div>
    <div class="h-sec">Maximum Cooking Time</div>
    <div class="pills off"><div class="pill">30 mins</div><div class="pill">1 hr</div><div class="pill">2 hrs</div></div>
    <div class="cta"><span class="tick">✓</span>Get your recipe</div>
  </div>
  <div class="subscribe"><div class="bell"><i></i></div><p>Subscribe to add maximum cooking time</p></div>
  <div class="home-bar"></div>
</section>

<!-- Choose cuisine -->
<section class="screen" style="left:933px;top:730px;height:810px">
  <div class="status light"><span>9:41</span><svg viewBox="0 0 36 9" fill="#fff"><rect x="0" y="5" width="2" height="4"/><rect x="3" y="3" width="2" height="6"/><rect x="6" y="1" width="2" height="8"/><rect x="24" y="1" width="11" height="7" rx="2"/></svg></div>
  <div class="hdr"><div class="hdr-title">Get a recipe</div><div class="round-btn left"><svg viewBox="0 0 10 10"><path d="M8 5H2M5 2L2 5l3 3" stroke="#fff" fill="none"/></svg></div></div>
  <div class="hero small" role="img" aria-label="Recipe illustration with herbs and vegetables"></div>
  <div class="pad" style="margin-top:68px">
    <div class="h-sec">Customize your recipe</div>
    <div class="tabs"><div class="tab"><svg viewBox="0 0 12 12"><path d="M2 10l7-7 1 1-7 7z" fill="#ccc"/></svg>Add Ingredients</div><div class="tab on"><svg viewBox="0 0 12 12"><path d="M1 9h10M2 9a4 4 0 018 0" fill="#ee7325"/></svg>Cuisine</div><div class="tab"><svg viewBox="0 0 12 12"><rect x="2" y="5" width="8" height="5" fill="#ccc"/></svg>Occasion</div></div>
    <div class="h-sec">Choose your cuisine</div>
    <div class="cuisines">
      <div class="cuisine">American</div><div class="cuisine">Italian</div>
      <div class="cuisine">Mexican</div><div class="cuisine">Japanese</div>
      <div class="cuisine on">Arab</div><div class="cuisine">British</div>
      <div class="cuisine">Chinese</div><div class="cuisine">French</div>
      <div class="cuisine">Thai</div><div class="cuisine">Greek</div>
      <div class="cuisine">Spanish</div><div class="cuisine">Asian</div>
      <div class="cuisine">German</div><div class="cuisine">Cuban</div>
    </div>
    <div class="h-sec">Avoid ingredients</div>
    <div class="list">
      <div class="list-row">Pork<span class="x">×</span></div>
      <div class="list-row">Peanut<span class="x">×</span></div>
      <div class="add-row"><span class="plus">+</span>ingredient</div>
    </div>
    <div class="h-sec">Maximum Cooking Time</div>
    <div class="pills off"><div class="pill">30 mins</div><div class="pill">1 hr</div><div class="pill">2 hrs</div></div>
    <div class="cta"><span class="tick">✓</span>Get your recipe</div>
  </div>
  <div class="subscribe"><div class="bell"><i></i></div><p>Subscribe to add maximum cooking time</p></div>
  <div class="home-bar"></div>
</section>

<!-- Details 1: ingredients -->
<section class="screen" style="left:195px;top:1610px;height:940px">
  <div class="status light"><span>9:41</span><svg viewBox="0 0 36 9" fill="#fff"><rect x="0" y="5" width="2" height="4"/><rect x="3" y="3" width="2" height="6"/><rect x="6" y="1" width="2" height="8"/><rect x="24" y="1" width="11" height="7" rx="2"/></svg></div>
  <div class="hdr" style="height:105px"><div class="round-btn left"><svg viewBox="0 0 10 10"><path d="M8 5H2M5 2L2 5l3 3" stroke="#fff" fill="none"/></svg></div><div class="round-btn right"><svg viewBox="0 0 10 10"><path d="M3 2h4v6L5 6.5 3 8z" stroke="#fff" fill="none"/></svg></div></div>
  <div class="hero big" role="img" aria-label="Photo of beef curry in a bowl"></div>
  <div class="pad" style="margin-top:62px">
    <div class="d-kicker">Recipe details</div>
    <div class="d-title">Name of recipe placeholder</div>
    <div class="info"><div><span class="ic"></span><span><small>CUISINE TYPE</small><b>Mexican</b></span></div><div><span class="ic"></span><span><small>COOKING TIME</small><b>20 mins</b></span></div></div>
    <div class="acc open">Ingredients<svg viewBox="0 0 9 9"><path d="M1 6l3.5-3.5L8 6" stroke="#ee7325" fill="none"/></svg></div>
    <div class="sub">COOK BEEF:</div>
    <div class="ing">
      <p>1/2 cup sliced onion</p><p>3 garlic cloves, chopped</p><p>1" fresh ginger, chopped</p><p>1/2 tsp ground turmeric (turmeric powder)</p><p>1 tbsp ground coriander (coriander powder)</p><p>1 tbsp garam masala</p><p>1 tsp red chili powder</p><p>1 kg gravy or chuck steak cut into 2.5 cm cubes</p><p>1/4 cup coconut slices (optional)</p><p>Salt to taste</p>
    </div>
    <div class="sub">TEMPERED SPICES TO ADD TO BEEF CURRY:</div>
    <div class="ing" style="margin-bottom:26px">
      <p>2 tbsp oil</p><p>1 tsp mustard seeds</p><p>2 dried bay leaves</p><p>1 cinnamon stick</p><p>1 cup chopped onions</p><p>1/4 tsp ground turmeric (turmeric powder)</p><p>1 tsp ground coriander (coriander powder)</p><p>2 tsp garam masala</p><p>1/2 tsp red chili powder</p><p>Water</p><p>Salt to taste</p><p>1/4 cup chopped coriander (cilantro) leaves</p>
    </div>
    <div class="acc">Preparation<svg viewBox="0 0 9 9"><path d="M1 3l3.5 3.5L8 3" stroke="#ee7325" fill="none"/></svg></div>
    <div class="acc">Nutritional information<svg viewBox="0 0 9 9"><path d="M1 3l3.5 3.5L8 3" stroke="#ee7325" fill="none"/></svg></div>
    <div class="cta">↻ Get New Recipe</div>
  </div>
  <div class="home-bar"></div>
</section>

<!-- Details 2: preparation -->
<section class="screen" style="left:490px;top:1610px;height:940px">
  <div class="status light"><span>9:41</span><svg viewBox="0 0 36 9" fill="#fff"><rect x="0" y="5" width="2" height="4"/><rect x="3" y="3" width="2" height="6"/><rect x="6" y="1" width="2" height="8"/><rect x="24" y="1" width="11" height="7" rx="2"/></svg></div>
  <div class="hdr" style="height:105px"><div class="round-btn left"><svg viewBox="0 0 10 10"><path d="M8 5H2M5 2L2 5l3 3" stroke="#fff" fill="none"/></svg></div><div class="round-btn right"><svg viewBox="0 0 10 10"><path d="M3 2h4v6L5 6.5 3 8z" fill="#fff"/></svg></div></div>
  <div class="hero big" role="img" aria-label="Photo of beef curry in a bowl"></div>
  <div class="pad" style="margin-top:62px">
    <div class="d-kicker">Recipe details</div>
    <div class="d-title">Name of recipe placeholder</div>
    <div class="info"><div><span class="ic"></span><span><small>CUISINE TYPE</small><b>Mexican</b></span></div><div><span class="ic"></span><span><small>COOKING TIME</small><b>20 mins</b></span></div></div>
    <div class="acc">Ingredients<svg viewBox="0 0 9 9"><path d="M1 3l3.5 3.5L8 3" stroke="#ee7325" fill="none"/></svg></div>
    <div class="acc open">Preparation<svg viewBox="0 0 9 9"><path d="M1 6l3.5-3.5L8 6" stroke="#ee7325" fill="none"/></svg></div>
    <div class="sub">COOK BEEF:</div>
    <div class="step"><b>01</b><p>To cook beef over stove top, place diced beef, onions, garlic, ginger, ground turmeric, ground coriander, garam masala and red chili powder in a large frying pan. Season with salt. Cover with water. Cook for 1 hour or until beef is tender</p></div>
    <div class="step"><b>02</b><p>(To cook in a pressure cooker, place diced beef, sliced onions, garlic, ginger, ground turmeric, ground coriander, garam masala, red chili powder and coconut slices (if using) in a pressure cooker. Season with salt. Stir to combine. Cook, covered, until 5-6 whistles. Remove from heat. Release pressure. Set aside.)</p></div>
    <div class="sub" style="margin-top:14px">TEMPERED SPICES TO ADD TO BEEF CURRY:</div>
    <div class="step"><b>01</b><p>Heat oil in a large frying pan over medium-high heat. Add mustard seeds and allow to splutter. Add bay leaves and cinnamon stick. Sauté, stirring constantly, for few seconds. Add onions. Sauté, stirring occasionally, for 3-4 minutes or until browned.</p></div>
    <div class="step"><b>02</b><p>Add ground turmeric, ground coriander, garam masala and red chili powder. Sauté, stirring constantly, for a minute. Season with salt. Add water to make thick sauce. Bring to boil. Simmer 2-3 minutes.</p></div>
    <div class="step"><b>03</b><p>Add cooked beef. Stir to combine. Add chopped coriander (cilantro) leaves. Simmer 5-6 minutes.</p></div>
    <div class="step" style="margin-bottom:22px"><b>04</b><p>Garnish with more coriander (cilantro) leaves if you like.</p></div>
    <div class="acc">Nutritional information<svg viewBox="0 0 9 9"><path d="M1 3l3.5 3.5L8 3" stroke="#ee7325" fill="none"/></svg></div>
    <div class="cta">↻ Get New Recipe</div>
  </div>
  <div class="home-bar"></div>
</section>

<!-- Details 3: nutrition -->
<section class="screen" style="left:785px;top:1610px;height:940px">
  <div class="status light"><span>9:41</span><svg viewBox="0 0 36 9" fill="#fff"><rect x="0" y="5" width="2" height="4"/><rect x="3" y="3" width="2" height="6"/><rect x="6" y="1" width="2" height="8"/><rect x="24" y="1" width="11" height="7" rx="2"/></svg></div>
  <div class="hdr" style="height:105px"><div class="round-btn left"><svg viewBox="0 0 10 10"><path d="M8 5H2M5 2L2 5l3 3" stroke="#fff" fill="none"/></svg></div><div class="round-btn right"><svg viewBox="0 0 10 10"><path d="M3 2h4v6L5 6.5 3 8z" stroke="#fff" fill="none"/></svg></div></div>
  <div class="hero big" role="img" aria-label="Photo of beef curry in a bowl"></div>
  <div class="pad" style="margin-top:62px">
    <div class="d-kicker">Recipe details</div>
    <div class="d-title">Name of recipe placeholder</div>
    <div class="info"><div><span class="ic"></span><span><small>CUISINE TYPE</small><b>Mexican</b></span></div><div><span class="ic"></span><span><small>COOKING TIME</small><b>20 mins</b></span></div></div>
    <div class="acc">Ingredients<svg viewBox="0 0 9 9"><path d="M1 3l3.5 3.5L8 3" stroke="#ee7325" fill="none"/></svg></div>
    <div class="acc">Preparation<svg viewBox="0 0 9 9"><path d="M1 3l3.5 3.5L8 3" stroke="#ee7325" fill="none"/></svg></div>
    <div class="acc open">Nutritional information<svg viewBox="0 0 9 9"><path d="M1 6l3.5-3.5L8 6" stroke="#ee7325" fill="none"/></svg></div>
    <div class="nut">
      <h2>NUTRITION<br>INFORMATION</h2>
      <div class="r" style="border:0;margin-top:6px"><b>Yield</b> 4</div>
      <div class="r" style="border:0"><b>Serving size</b> 1</div>
      <div class="thick"></div>
      <em>Amount Per Serving</em>
      <div class="r" style="border:0"><b>Calories</b> 299</div>
      <div class="thin"></div>
      <div class="r"><b>Total Fat</b> 20g</div>
      <div class="r in">Saturated Fat 5g</div>
      <div class="r in">Trans Fat 0g</div>
      <div class="r in">Unsaturated Fat 13g</div>
      <div class="r"><b>Cholesterol</b> 33g</div>
      <div class="r"><b>Sodium</b> 1330mg</div>
      <div class="r"><b>Carbohydrates</b> 30g</div>
      <div class="r in">Fiber 4g</div>
      <div class="r in">Sugar 7g</div>
      <div class="r" style="border:0"><b>Protein</b> 10g</div>
    </div>
    <div class="cta">↻ Get New Recipe</div>
  </div>
  <div class="home-bar"></div>
</section>

</body>
</html>
```